Flyer-Design für Musikverein - Jugendkapelle
Zielgruppe
Musikverein Hallbrunn
Unsere Zielgruppe sind Kinder und Jugendliche, die ein Instrument erlernen wollen.
Der Einstieg der jüngsten geht in einem Alter ab ca. 8 Jahren los. Die meisten neuen Musiker steigen zwischen 10 - 14 Jahren ein.
Der Flyer soll aber auch geeignet sein um an Grund- und weiterführenden Schulen ausgelegt werden zu können um Musiker für die Jugendkapelle zu gewinnen. Dementsprechend frisch und interessant soll der Flyer gestaltet sein.
Aufgabenstellung
Es soll ansprechend sein für Jugendliche, frisch, fröhlich und soll das Interesse der jugendlichen mit dem Design wecken.
Es soll die Jugendlichkeit, die Blasmusik und das Vereinsleben miteinander verbinden, sowie die Vorteile und der Spaß an der Musik (Instrument erlernen, Spaß am Musizieren, neue Freunde und Kameradschaft und auch Freizeitaktivitäten) miteinander darstellen.

```html
<!DOCTYPE html>
<html lang="de">
<head>
<meta charset="utf-8">
<title>Musik macht Freu(n)de – Musikverein Hallbrunn</title>
<link rel="stylesheet" href="https://fonts.googleapis.com/css2?family=Amatic+SC:wght@700&family=Caveat+Brush&family=Work+Sans:wght@400;500;700&display=swap">
<style>
  :root {
    --sun: #F9C559;
    --orange: #EC7A34;
    --orange-soft: #F08F45;
    --accent-text: #E9692A;
    --highlight: #FCE35C;
    --white: #FFFFFF;
    --cream: #FFF6DC;
  }
  * { margin: 0; padding: 0; box-sizing: border-box; }
  html, body { width: 1200px; height: 2572px; overflow: hidden; background: var(--sun); }
  .flyer {
    position: relative; width: 1200px; height: 2572px; overflow: hidden;
    background: var(--sun);
    font-family: "Work Sans", Arial, sans-serif; color: var(--white);
    letter-spacing: 0.04em;
  }
  .backdrop { position: absolute; inset: 0; }
  .headline { position: absolute; left: 0; top: 0; width: 1200px; height: 2572px; pointer-events: none; }
  .headline text { font-family: "Amatic SC", "Arial Narrow", sans-serif; font-weight: 700; }
  .headline .script { font-family: "Caveat Brush", cursive; }
  .headline .tag { font-family: "Work Sans", Arial, sans-serif; font-weight: 700; letter-spacing: 0.04em; }
  .art { position: absolute; border-radius: 14px; }
  .art--notes { left: 960px; top: 100px; width: 120px; height: 130px; background: radial-gradient(circle, rgba(40,30,20,0.22), rgba(40,30,20,0) 70%); }
  .art--trumpet { left: 350px; top: 1900px; width: 110px; height: 140px; background: rgba(255,246,220,0.5); transform: rotate(35deg); }
  .art--trombone { left: 735px; top: 2060px; width: 170px; height: 50px; background: rgba(255,246,220,0.5); transform: rotate(-22deg); }
  .art--drum { left: 495px; top: 2320px; width: 100px; height: 95px; background: rgba(255,246,220,0.7); border-radius: 40%; }
  .intro-question { position: absolute; left: 108px; top: 362px; font-size: 43px; line-height: 50px; }
  .copy { position: absolute; left: 106px; width: 1000px; font-size: 40px; line-height: 50px; }
  .copy strong { font-weight: 700; letter-spacing: 0.01em; }
  .copy--invite { top: 580px; }
  .copy--offer { top: 730px; }
  .section-title { position: absolute; left: 106px; top: 968px; font-size: 44px; font-weight: 700; color: var(--accent-text); letter-spacing: 0.01em; }
  .bullets { position: absolute; left: 230px; list-style: none; }
  .bullets li { position: relative; }
  .bullets li::before {
    content: ""; position: absolute; left: -46px; width: 19px; height: 18px;
    background: var(--accent-text); border-radius: 5px 3px 6px 4px; transform: rotate(-8deg);
  }
  .services { top: 1062px; width: 800px; font-size: 39px; line-height: 51px; font-weight: 400; }
  .services li::before { top: 16px; }
  .about { position: absolute; left: 106px; top: 1384px; width: 960px; font-size: 38px; line-height: 48px; font-weight: 400; }
  .about strong { color: var(--accent-text); font-weight: 700; letter-spacing: 0.01em; }
  .instruments { top: 1946px; font-size: 43px; line-height: 58px; font-weight: 700; color: var(--accent-text); letter-spacing: 0.02em; }
  .instruments li::before { top: 21px; }
</style>
</head>
<body>
<div class="flyer">
  <svg class="backdrop" width="1200" height="2572" viewBox="0 0 1200 2572" aria-hidden="true">
    <defs>
      <linearGradient id="wash-top" x1="0" y1="0" x2="1" y2="1">
        <stop offset="0" stop-color="#EF7F37"/>
        <stop offset="0.6" stop-color="#F08C45"/>
        <stop offset="1" stop-color="#F39A52"/>
      </linearGradient>
      <linearGradient id="wash-bottom" x1="0" y1="0" x2="1" y2="1">
        <stop offset="0" stop-color="#F08C45"/>
        <stop offset="1" stop-color="#EE8139"/>
      </linearGradient>
    </defs>
    <path fill="url(#wash-top)" d="M0 205 C160 195 320 215 470 225 C640 240 820 300 900 380 C960 440 990 470 960 520 C930 560 850 545 780 590 C720 640 760 720 700 770 C640 820 520 850 420 880 C320 905 200 900 110 880 C60 860 20 840 0 835 Z"/>
    <path fill="url(#wash-bottom)" d="M1200 1940 C1130 1980 1050 2050 1010 2140 C970 2230 990 2320 940 2400 C905 2460 890 2520 900 2572 L1200 2572 Z"/>
  </svg>

  <div class="art art--notes" role="img" aria-label="Kleine Musiknoten als Dekoration"></div>

  <svg class="headline" width="1200" height="2572" viewBox="0 0 1200 2572">
    <text x="114" y="330" font-size="172" fill="#FFFFFF" stroke="#FFFFFF" stroke-width="5" textLength="885" lengthAdjust="spacingAndGlyphs">MUSIK MACHT</text>
    <g transform="rotate(-4 850 390)">
      <rect x="640" y="340" width="450" height="105" fill="#FCE35C"/>
      <text x="648" y="438" font-size="126" fill="#FFF6DC" stroke="#FFF6DC" stroke-width="4" textLength="432" lengthAdjust="spacingAndGlyphs">FREU(N)DE</text>
    </g>
    <text class="script" x="110" y="1758" font-size="100" fill="#FFFFFF" textLength="765" lengthAdjust="spacingAndGlyphs">Folgende Instrumente</text>
    <g transform="rotate(-4 795 1800)">
      <rect x="495" y="1776" width="610" height="64" fill="#FCE35C"/>
      <text class="tag" x="520" y="1824" font-size="44" fill="#FFFFFF" textLength="570" lengthAdjust="spacingAndGlyphs">können erlernt werden:</text>
    </g>
  </svg>

  <p class="intro-question">Wer von euch will<br><strong>Musiker</strong> werden?</p>

  <p class="copy copy--invite">Probiere es bei uns aus, beim <strong>MV HALLBRUNN.</strong><br><strong>Hast du Lust, bei uns mitzumachen?</strong></p>

  <p class="copy copy--offer">Wir bieten im Bereich Blasmusik quali-<br>fizierten Musikunterricht für <strong>Kinder und<br>Jugendliche</strong> an.</p>

  <h2 class="section-title">Unsere Leistungen:</h2>
  <ul class="bullets services">
    <li>Einzelunterricht</li>
    <li>Lehrkräfte mit Musikausbildung und langjähriger pädagogischer Erfahrung</li>
    <li>Unterrichtsbeginn immer am Monats-<br>anfang</li>
  </ul>

  <p class="about">Der <strong>Musikverein Hallbrunn e.V.</strong> bietet allen musikinteressierten Kindern, Jugendlichen und Erwachsenen die Möglichkeit, ein Instrument zu erlernen.</p>

  <div class="art art--trumpet" role="img" aria-label="Zeichnung einer Trompete"></div>
  <div class="art art--trombone" role="img" aria-label="Zeichnung einer Posaune"></div>

  <ul class="bullets instruments">
    <li>Trompete / Flügelhorn</li>
    <li>Tuba</li>
    <li>Tenorhorn / Bariton / Posaune</li>
    <li>Waldhorn</li>
    <li>Klarinette / Saxophon</li>
    <li>Querflöte</li>
    <li>Schlagzeug</li>
  </ul>

  <div class="art art--drum" role="img" aria-label="Zeichnung einer Trommel"></div>
</div>
</body>
</html>
```